Entrepreneur needs a business card design

I need a business card to name my three companies, as well as contact information.
I'm open on design and color and it can be plain or complex. I'm open on colors but I think I prefer something somewhat formal but fun as well.
I'm open on whether the background is plain or has design in it. I don't have company logos.
Target Market(s)
Auto dealers, realtors and property managers
Industry/Entity Type
Business
Contact Information for Business Card
HOLLISTER FAMILY PROPERTIES, LLC
HOLLISTER PUBLISHING, LLC
LOTMASTER CONSULTING, LLC
Ned Hollister
2847 W. Tamarack Ave. #310
Boise, Idaho 83611-2905
208-514-3092
ned@holl5x.example

```html
<!DOCTYPE html>
<html lang="en">
<head>
<meta charset="utf-8">
<title>Hollister Business Card</title>
<link rel="stylesheet" href="https://fonts.googleapis.com/css2?family=Jost:wght@300;400&display=swap">
<style>
  :root {
    --canvas-bg: #eef0f1;
    --card-white: #ffffff;
    --band-grey: #d4d5d7;
    --panel-teal: #0cb1b0;
    --ink-grey: #5a5b5d;
    --ink-white: #ffffff;
  }
  * { margin: 0; padding: 0; box-sizing: border-box; }
  html, body {
    width: 1200px;
    height: 1200px;
    overflow: hidden;
    background: var(--canvas-bg);
  }
  .stage {
    width: 1200px;
    height: 1200px;
    display: flex;
    align-items: center;
    justify-content: center;
  }
  .card {
    position: relative;
    width: 1050px;
    height: 600px;
    background: var(--card-white);
    overflow: hidden;
    box-shadow: 0 2px 10px rgba(0, 0, 0, 0.08);
    font-family: "Jost", "Futura", sans-serif;
  }
  .accent-band {
    position: absolute;
    top: 0;
    right: 0;
    width: 440px;
    height: 100%;
    background: var(--band-grey);
  }
  .contact-panel {
    position: absolute;
    top: 52px;
    left: 545px;
    width: 395px;
    height: 496px;
    background: var(--panel-teal);
    color: var(--ink-white);
    display: flex;
    flex-direction: column;
    justify-content: center;
    align-items: flex-end;
    padding: 0 44px;
    text-align: right;
    font-weight: 300;
  }
  .contact-panel p {
    font-size: 27px;
    line-height: 1.32;
    letter-spacing: 0.3px;
  }
  .contact-panel .contact-email {
    font-size: 21px;
    margin-top: 6px;
  }
  .company-list {
    position: absolute;
    top: 0;
    left: 0;
    width: 545px;
    height: 100%;
    display: flex;
    flex-direction: column;
    justify-content: center;
    align-items: center;
    gap: 38px;
    list-style: none;
    color: var(--ink-grey);
    text-align: center;
    font-weight: 300;
  }
  .company-list li {
    font-size: 30px;
    line-height: 1.25;
    letter-spacing: 1.5px;
    text-transform: uppercase;
  }
</style>
</head>
<body>
  <main class="stage">
    <article class="card">
      <ul class="company-list">
        <li>Hollister Family<br>Properties, LLC</li>
        <li>Hollister<br>Publishing, LLC</li>
        <li>Lotmaster<br>Consulting, LLC</li>
      </ul>
      <div class="accent-band"></div>
      <address class="contact-panel" style="font-style: normal;">
        <p class="contact-name">Ned Hollister</p>
        <p>2847 W. Tamarack Ave.</p>
        <p>#310 Boise,</p>
        <p>Idaho 83611-2905</p>
        <p>208-514-3092</p>
        <p class="contact-email">ned@holl5x.example</p>
      </address>
    </article>
  </main>
</body>
</html>
```